Brindle Water - 500ml

to create a water bottle packaging similar to La Roche Vive design. Bottle should be blue similar to PURE CLOUD but change the design/logo to Brindle. Wording should be similar just different design and logo. Thanks.

Colors
0054AA
0677BA
7BADD7
CADEEF
E8F1F8

Requirements
Must have
• Bottle must not be in plastic bottles. They are made in a carton instead - see PURE CLOUD for reference.

```html
<!DOCTYPE html>
<html lang="en">
<head>
<meta charset="utf-8">
<title>Brindle Water – Pure Cloud 500ml Carton</title>
<link rel="stylesheet" href="https://fonts.googleapis.com/css2?family=Oswald:wght@400;500;600;700&display=swap">
<style>
  :root {
    --carton-blue: #2eb1e2;
    --navy: #0054aa;
    --mid-blue: #0677ba;
    --soft-blue: #7badd7;
    --pale-blue: #cadeef;
    --ice: #e8f1f8;
    --white: #ffffff;
    --backdrop: #eef1f4;
  }
  * { box-sizing: border-box; margin: 0; padding: 0; }
  html, body {
    width: 1200px;
    height: 3000px;
    overflow: hidden;
    background: var(--backdrop);
    font-family: "Oswald", "Arial Narrow", sans-serif;
    color: var(--white);
  }
  .panel {
    position: absolute;
    background: var(--carton-blue);
    overflow: hidden;
    text-align: center;
  }
  .mountains {
    position: absolute;
    left: 0; right: 0; bottom: 0;
    background: linear-gradient(to bottom, rgba(255,255,255,0) 0%, rgba(255,255,255,0.75) 30%, var(--white) 60%);
  }

  /* front */
  .front { left: 290px; top: 60px; width: 620px; height: 1400px; }
  .brand { margin-top: 110px; }
  .brand-name {
    font-size: 92px; font-weight: 600; color: var(--navy);
    line-height: 1; letter-spacing: 1px;
  }
  .brand-line {
    margin-top: 10px; font-size: 15px; font-weight: 400;
    color: var(--navy); letter-spacing: 2px;
  }
  .product-name {
    margin-top: 36px; font-size: 212px; font-weight: 600;
    line-height: 0.98; letter-spacing: 2px;
  }
  .claim {
    margin-top: 34px; font-size: 52px; font-weight: 600; line-height: 1.1;
  }
  .rule { width: 400px; height: 2px; background: var(--white); margin: 22px auto 18px; opacity: 0.85; }
  .sub-claim { font-size: 30px; font-weight: 600; line-height: 1.22; letter-spacing: 1px; }
  .front .mountains { height: 370px; }
  .volume {
    position: absolute; left: 40px; bottom: 50px; width: 190px; height: 250px;
  }
  .volume svg { position: absolute; inset: 0; }
  .volume-text {
    position: absolute; left: 0; right: 0; top: 110px;
    font-size: 50px; font-weight: 700; line-height: 0.95; color: var(--white);
  }

  /* side panels */
  .side { top: 1540px; width: 360px; height: 1400px; padding: 70px 36px 0; }
  .side-one { left: 45px; }
  .side-two { left: 420px; }
  .side-three { left: 795px; }
  .side .mountains { height: 300px; }

  .fact-list { list-style: none; }
  .fact-list li { margin-bottom: 46px; }
  .fact-list svg { width: 46px; height: 46px; display: block; margin: 0 auto 12px; }
  .fact-list p { font-size: 17px; font-weight: 400; line-height: 1.3; letter-spacing: 1px; }

  .badges {
    display: grid; grid-template-columns: 1fr 1fr; gap: 24px;
    width: 260px; margin: 0 auto 50px;
  }
  .badge { width: 118px; height: 118px; border: 3px solid var(--white); border-radius: 50%; }
  .badge.square { border-radius: 10px; }
  .section-title { font-size: 26px; font-weight: 600; letter-spacing: 1px; margin-bottom: 14px; }
  .body-copy { font-size: 16px; line-height: 1.45; letter-spacing: 0.5px; margin-bottom: 36px; }
  .contact { font-size: 19px; font-weight: 600; line-height: 1.45; letter-spacing: 1px; }

  .side-three { text-align: left; }
  .analysis { width: 100%; border-collapse: collapse; font-size: 18px; margin-bottom: 46px; }
  .analysis td { padding: 3px 0; border-bottom: 1px solid rgba(255,255,255,0.5); }
  .analysis td:last-child { text-align: right; }
  .notice {
    border: 2px solid var(--white); padding: 22px 18px;
    text-align: center; font-size: 16px; font-weight: 600; line-height: 1.4;
  }
  .notice p + p { margin-top: 18px; }
</style>
</head>
<body>

<section class="panel front">
  <div class="brand">
    <div class="brand-name">Brindle</div>
    <div class="brand-line">BEVERAGES | EST CIRCA 1860</div>
  </div>
  <h1 class="product-name">PURE<br>CLOUD</h1>
  <p class="claim">100%<br>SPRING WATER</p>
  <div class="rule"></div>
  <p class="sub-claim">SUSTAINABLY SOURCED WATER<br>IN A PLANT-BASED<br>CARTON</p>
  <div class="mountains" role="img" aria-label="White snow-capped mountain range silhouette"></div>
  <div class="volume">
    <svg viewBox="0 0 190 250" aria-hidden="true">
      <path d="M95 8 C120 70 175 120 175 165 A80 80 0 0 1 15 165 C15 120 70 70 95 8 Z" fill="var(--carton-blue)" stroke="var(--white)" stroke-width="8"/>
    </svg>
    <div class="volume-text">500<br>ML</div>
  </div>
</section>

<section class="panel side side-one">
  <ul class="fact-list">
    <li>
      <svg viewBox="0 0 46 46" fill="none" stroke="#fff" stroke-width="2.5"><path d="M23 5 C30 17 36 23 36 30 A13 13 0 0 1 10 30 C10 23 16 17 23 5 Z"/></svg>
      <p>PURE CLOUD IS WATER IN ITS SIMPLEST FORM.</p>
    </li>
    <li>
      <svg viewBox="0 0 46 46" fill="none" stroke="#fff" stroke-width="2.5"><circle cx="23" cy="23" r="17"/><path d="M15 23 l6 6 l11 -12"/></svg>
      <p>100% AUSTRALIAN SPRING WATER AND A CARTON LIKE NO OTHER.</p>
    </li>
    <li>
      <svg viewBox="0 0 46 46" fill="none" stroke="#fff" stroke-width="2.5"><path d="M10 36 C10 16 24 8 38 8 C38 24 30 36 10 36 Z"/><path d="M10 36 L28 18"/></svg>
      <p>IT'S MADE FROM 77% PAPER.</p>
    </li>
    <li>
      <svg viewBox="0 0 46 46" fill="none" stroke="#fff" stroke-width="2.5"><path d="M6 38 L16 20 L24 30 L30 22 L40 38 Z"/></svg>
      <p>TOTALLING 87% RENEWABLE CONTENT.</p>
    </li>
    <li>
      <svg viewBox="0 0 46 46" fill="none" stroke="#fff" stroke-width="2.5"><rect x="14" y="12" width="18" height="28" rx="2"/><path d="M18 12 V6 H28 V12"/></svg>
      <p>ALL THAT AND IT'S STILL RECYCLABLE.</p>
    </li>
    <li>
      <svg viewBox="0 0 46 46" fill="none" stroke="#fff" stroke-width="2.5"><path d="M10 24 A13 13 0 0 1 36 24"/><path d="M36 24 A13 13 0 0 1 10 24"/><path d="M32 16 l4 8 l-8 0"/></svg>
      <p>WE BUILD LESS PLASTIC IN THE WORLD AND REDUCE CARBON EMISSIONS.</p>
    </li>
  </ul>
  <div class="mountains" role="img" aria-label="White snow-capped mountain range silhouette"></div>
</section>

<section class="panel side side-two">
  <div class="badges">
    <div class="badge"></div>
    <div class="badge square"></div>
    <div class="badge"></div>
    <div class="badge"></div>
  </div>
  <h2 class="section-title">YOU JUST DID A GOOD THING</h2>
  <p class="body-copy">This carton is made mainly from plants, which pull CO2 from the air instead of adding more. It's recyclable when you have finished with it too. Sure, it's not perfect, but it's a better option. So if you're going to buy packaged water, this one's better for everyone.</p>
  <p class="contact">WEBSITE &amp; SOCIAL<br>BRINDLEWATER.COM.AU<br>TWITTER: @BRINDLEPURE<br>INSTAGRAM: @BRINDLEWATER</p>
  <div class="mountains" role="img" aria-label="White snow-capped mountain range silhouette"></div>
</section>

<section class="panel side side-three">
  <h2 class="section-title">TYPICAL WATER ANALYSIS (MG/L)</h2>
  <table class="analysis">
    <tr><td>CALCIUM</td><td>17</td></tr>
    <tr><td>MAGNESIUM</td><td>2.3</td></tr>
    <tr><td>POTASSIUM</td><td>1.2</td></tr>
    <tr><td>SODIUM</td><td>9</td></tr>
    <tr><td>CHLORIDE</td><td>6.6</td></tr>
    <tr><td>OXIDISED NITROGEN</td><td>0.6</td></tr>
    <tr><td>SILICA</td><td>15</td></tr>
    <tr><td>BICARBONATE</td><td>50</td></tr>
  </table>
  <h2 class="section-title">PACKAGING FACTS</h2>
  <table class="analysis">
    <tr><td>PAPER</td><td>68%</td></tr>
    <tr><td>PLANT-BASED PLASTIC</td><td>22%</td></tr>
    <tr><td>PE PLASTIC</td><td>5%</td></tr>
    <tr><td>FOIL</td><td>5%</td></tr>
  </table>
  <div class="notice">
    <p>PLEASE CLOSE THE LID AND RECYCLE.<br>DO NOT CRUSH OR FLATTEN.</p>
    <p>PROUD BRAND OF<br>BRINDLE SPRING WATER</p>
  </div>
  <div class="mountains" role="img" aria-label="White snow-capped mountain range silhouette"></div>
</section>

</body>
</html>
```